Flyer to promote new Commercial HVAC Preventative Maintenance clients

This flyer will be in the body of emails that will be sent to new, existing, and/or potential commericial buildings HVAC clients. It will have the least amount of words used, but it will convey the point with pertinent pictorial and graphics. It will show the value of a Periodic/Preventative routine maintenance to lower operating costs of their commericial buildings (i.e. office, medical, shopping centers, apartment, warehouse facility, etc.), in the following ways:
1) Reduce monthly power usage,
2) Reduce emergency HVAC service calls,
3) Reduce costly repairs costs,
4) Reduce HVAC down-times and angry tenants,
5) Increases the life expectancy of the existing and/or new HVAC equipment in the building and/or the equipment's' early replacement costs,
6) Reduces tenant's early termination of their lease and law suits against the landlords,
7) Increases tenant's renewal of the lease and agree to pay the increase rental rates,
8) Reduces unhappy customers and increases tenant's productivity,
9) By reducing the landlord's expenses, the value of the property will increase considerably and profitable to sell their holdings, or refinance and keep their holdings with an increased ROI (Return On Investment).

Landlords can not depend on their tenants' obligation to maintain the landlords' major assets, which is their HVAC equipment and systems.

With the periodic maintenance done by one reliable and licensed HVAC company, the will not use different companies that may or may not do the right repair job on their unit and hurt their bottom line and increase HVAC replacement COSTLY rates.

```html
<!DOCTYPE html>
<html lang="en">
<head>
<meta charset="utf-8">
<title>Routine HVAC Maintenance Flyer</title>
<link href="https://fonts.googleapis.com/css2?family=Bebas+Neue&family=Poppins:wght@500;600&display=swap" rel="stylesheet">
<style>
  :root{
    --navy:#0c5186;
    --header-blue:#1d5fa3;
    --header-deep:#0f3f78;
    --yellow:#ffe21a;
    --orange:#f9b12d;
    --row-grey:#f2f2f2;
    --row-blue:#c1dcf0;
    --ink:#1b1b2b;
    --white:#ffffff;
  }
  *{margin:0;padding:0;box-sizing:border-box}
  html,body{width:697px;height:1200px;overflow:hidden;background:var(--white)}
  body{font-family:"Poppins",sans-serif;color:var(--ink);position:relative}
  .flyer{position:absolute;left:81px;top:81px;width:533px;height:1000px;background:var(--row-grey);box-shadow:0 4px 18px rgba(0,0,0,.12);overflow:hidden}
  .header{position:absolute;left:0;top:0;width:533px;height:143px;
    background:
      linear-gradient(180deg,rgba(12,60,120,.15) 0,rgba(12,60,120,0) 30%,rgba(20,80,150,.25) 100%),
      linear-gradient(100deg,#154a8a 0%,#1c5a9e 30%,#2c6aa8 55%,#1d5fa3 75%,#2a6fb3 100%)}
  .rooftop{position:absolute;left:0;top:0;width:533px;height:143px;background:radial-gradient(ellipse at 75% 80%,rgba(140,180,220,.35),rgba(140,180,220,0) 55%),radial-gradient(ellipse at 20% 30%,rgba(90,130,180,.35),rgba(90,130,180,0) 50%)}
  .title{position:absolute;left:31px;top:40px;color:var(--white);line-height:1}
  .title .lead{font-size:14.5px;font-weight:500;letter-spacing:-.2px}
  .title .accent{font-size:23px;font-weight:600;color:var(--yellow);letter-spacing:-.5px;margin-top:1px}
  .title .big{font-family:"Bebas Neue",sans-serif;font-size:31px;margin-top:2px;letter-spacing:-.2px}
  .divider{position:absolute;left:304px;top:42px;width:1px;height:64px;background:var(--yellow)}
  .at-your{position:absolute;left:323px;top:43px;font-size:10.5px;font-weight:600;color:var(--white);letter-spacing:-.2px}
  .at-your span{color:var(--yellow)}
  .at-your::after{content:"";display:block;margin-top:3px;border-bottom:1px dashed rgba(255,255,255,.6);width:162px}
  .types{position:absolute;top:64px;left:0;width:533px}
  .type{position:absolute;width:50px;margin-left:-25px;text-align:center;color:var(--white);font-family:"Bebas Neue",sans-serif;font-size:12px;line-height:1}
  .type svg{display:block;margin:0 auto 5px}
  .row{position:absolute;left:0;width:533px}
  .row.grey{background:var(--row-grey)}
  .row.blue{background:var(--row-blue)}
  .art{position:absolute}
  .point{position:absolute;font-weight:600;font-size:14px;line-height:16.6px;letter-spacing:0}
  .callout{position:absolute;left:49px;top:830px;width:432px;height:59px;background:var(--orange);border-radius:10px;color:var(--navy);font-weight:600;font-size:12.2px;line-height:15px;text-align:center;display:flex;align-items:center;justify-content:center;z-index:2}
  .footer{position:absolute;left:0;top:856px;width:533px;height:144px;background:var(--navy)}
  .white-strip{position:absolute;left:0;top:838px;width:533px;height:18px;background:var(--white)}
  .closing{position:absolute;left:20px;top:903px;width:493px;text-align:center;color:var(--white);font-weight:500;font-size:12.7px;line-height:15px}
</style>
</head>
<body>
<main class="flyer">
  <header class="header">
    <div class="rooftop" role="img" aria-label="Rooftop HVAC units photo tinted blue"></div>
    <div class="title">
      <div class="lead">VALUE OF A PERIODIC/PREVENTATIVE</div>
      <div class="accent">ROUTINE MAINTENANCE</div>
      <div class="big">TO LOWER OPERATING COSTS</div>
    </div>
    <div class="divider"></div>
    <div class="at-your">AT YOUR <span>COMMERCIAL BUILDINGS</span></div>
    <div class="types">
      <div class="type" style="left:327px"><svg width="25" height="25" viewBox="0 0 25 25"><circle cx="12.5" cy="12.5" r="11.5" fill="#fff" stroke="#9fc3e6" stroke-width="1.5"/><rect x="8" y="7" width="9" height="12" fill="#2b4f7c"/></svg>OFFICE</div>
      <div class="type" style="left:363px"><svg width="25" height="25" viewBox="0 0 25 25"><circle cx="12.5" cy="12.5" r="11.5" fill="#fff" stroke="#9fc3e6" stroke-width="1.5"/><rect x="7" y="9" width="11" height="10" fill="#2b4f7c"/><rect x="11" y="5" width="3" height="5" fill="#2b4f7c"/></svg>MEDICAL</div>
      <div class="type" style="left:399px"><svg width="25" height="25" viewBox="0 0 25 25"><circle cx="12.5" cy="12.5" r="11.5" fill="#fff" stroke="#9fc3e6" stroke-width="1.5"/><rect x="6" y="10" width="13" height="9" fill="#2b4f7c"/><rect x="9" y="6" width="7" height="4" fill="#2b4f7c"/></svg>MALL</div>
      <div class="type" style="left:436px"><svg width="25" height="25" viewBox="0 0 25 25"><circle cx="12.5" cy="12.5" r="11.5" fill="#fff" stroke="#9fc3e6" stroke-width="1.5"/><path d="M6 19V11l6.5-5 6.5 5v8z" fill="#2b4f7c"/></svg>APARTMENT</div>
      <div class="type" style="left:483px"><svg width="25" height="25" viewBox="0 0 25 25"><circle cx="12.5" cy="12.5" r="11.5" fill="#fff" stroke="#9fc3e6" stroke-width="1.5"/><path d="M6 19V10l6.5-4 6.5 4v9h-3v-6H9v6z" fill="#2b4f7c"/></svg>WAREHOUSE</div>
    </div>
  </header>

  <section class="row grey" style="top:143px;height:112px">
    <div class="art" role="img" aria-label="Illustration of energy saving with battery, recycle arrows and leaves" style="left:33px;top:30px;width:93px;height:62px;border-radius:45% 45% 20% 20%;background:radial-gradient(circle at 50% 45%,#f08a84 0,#f3b1ac 30%,#c9d3f3 60%,rgba(201,211,243,0) 75%)"></div>
    <p class="point" style="left:134px;top:45px">Reduce monthly<br>power usage</p>
    <div class="art" role="img" aria-label="Illustration of a service call centre worker at a laptop" style="left:266px;top:24px;width:66px;height:68px;border-radius:50% 50% 8px 8px;background:linear-gradient(160deg,#f4c542 0,#f4c542 30%,#8e8fdc 60%,#f6d35c 100%)"></div>
    <p class="point" style="left:356px;top:41px">Reduce emergency<br>HVAC service calls</p>
  </section>

  <section class="row blue" style="top:255px;height:101px">
    <div class="art" role="img" aria-label="Illustration of workers repairing large gears beside an hourglass" style="left:33px;top:24px;width:93px;height:63px;border-radius:40% 40% 6px 6px;background:radial-gradient(circle at 45% 40%,#4d8fe0 0,#6da4e8 35%,#f3b93a 70%,rgba(243,185,58,0) 85%)"></div>
    <p class="point" style="left:133px;top:37px">Reduce costly<br>repairs costs</p>
    <div class="art" role="img" aria-label="Illustration of people beside a large stopwatch" style="left:251px;top:12px;width:93px;height:74px;border-radius:50%;background:radial-gradient(circle at 50% 48%,#fff 0,#fff 16%,#3f7fd0 20%,#3f7fd0 32%,#bcd4f2 38%,#e8c89a 80%,rgba(232,200,154,0) 82%)"></div>
    <p class="point" style="left:356px;top:20px">Reduce HVAC<br>down-times<br>and angry tenants</p>
  </section>

  <section class="row grey" style="top:356px;height:94px">
    <div class="art" role="img" aria-label="Illustration of technicians servicing appliances" style="left:33px;top:12px;width:115px;height:71px;background:linear-gradient(180deg,#e3e6eb 0,#d4d8de 60%,#a7aeb8 100%)"></div>
    <p class="point" style="left:155px;top:22px">Increases the life expectancy of the existing<br>and/or new HVAC equipment in the building<br>and/or the equipment's' early replacement costs</p>
  </section>

  <section class="row blue" style="top:450px;height:86px">
    <div class="art" role="img" aria-label="Illustration of a house and a lease checklist" style="left:33px;top:15px;width:112px;height:57px;border-radius:50% 50% 10px 10px;background:linear-gradient(180deg,#e8f3f1 0,#e8f3f1 35%,#f0b66a 60%,#5c8f6d 100%)"></div>
    <p class="point" style="left:155px;top:27px">Reduces tenant's early termination of their<br>lease and law suits against the landlords</p>
  </section>

  <section class="row grey" style="top:536px;height:83px">
    <div class="art" role="img" aria-label="Illustration of tenants by rising houses with an upward arrow" style="left:31px;top:12px;width:114px;height:57px;clip-path:polygon(0 35%,35% 25%,70% 0,100% 10%,100% 100%,0 100%);background:linear-gradient(180deg,#f4c56a 0,#8fa7dc 45%,#7b93d0 100%)"></div>
    <p class="point" style="left:156px;top:21px">Increases tenant's renewal of the lease and<br>agree to pay the increase rental rates</p>
  </section>

  <section class="row blue" style="top:619px;height:86px">
    <div class="art" role="img" aria-label="Illustration of a person choosing between sad and happy feedback" style="left:33px;top:7px;width:93px;height:72px;border-radius:12px 40% 40% 12px;background:linear-gradient(180deg,#6fa2dc 0,#9cc0ea 40%,#d7e8f7 100%)"></div>
    <p class="point" style="left:156px;top:23px">Reduces unhappy customers and increases<br>tenant's productivity</p>
  </section>

  <section class="row grey" style="top:705px;height:133px">
    <div class="art" role="img" aria-label="Illustration of a person watering a money tree" style="left:32px;top:16px;width:108px;height:97px;border-radius:50% 50% 4px 4px;background:radial-gradient(circle at 55% 40%,#f3b93a 0,#f3b93a 20%,#8cc98a 45%,#6cab70 70%,rgba(108,171,112,0) 72%)"></div>
    <p class="point" style="left:154px;top:23px">By reducing the landlord's expenses, the value<br>of the property will increase considerably and<br>profitable to sell their holdings, or refinance and<br>keep their holdings with an increased ROI<br>(Return On Investment)</p>
  </section>

  <div class="white-strip"></div>
  <div class="footer"></div>
  <div class="callout">Landlords can not depend on their tenants' obligation<br>to maintain the landlords' major assets, which is their HVAC<br>equipment and systems</div>
  <p class="closing">With the periodic maintenance done by one reliable and licensed HVAC company, we will not use different companies that may or may not do the right repair job on their unit and hurt their bottom line and increase HVAC replacement COSTLY rate</p>
</main>
</body>
</html>
```